Accounting firm needing business card / letterhead designed
Marcus L. Tembrook, CPA
marcus@lumenfiledesk.com
www.lumenfiledesk.com
482 E Larkin Ave Alder Falls, WI 53911
712-555-0172
Business

```html
<!DOCTYPE html>
<html lang="en">
<head>
<meta charset="utf-8">
<title>Lumen Filedesk – Business Card</title>
<link rel="stylesheet" href="https://fonts.googleapis.com/css2?family=Michroma&family=Roboto:wght@400&display=swap">
<style>
  :root {
    --backdrop: #1a1a1a;
    --navy: #2a2468;
    --navy-deep: #231e60;
    --navy-light: #4238a0;
    --green: #8cc63f;
    --ink: #444444;
    --paper-a: #f8f8f8;
    --paper-b: #e9e9e9;
    --white: #ffffff;
  }
  * { margin: 0; padding: 0; box-sizing: border-box; }
  html, body {
    width: 1200px; height: 960px; overflow: hidden;
    background: var(--backdrop);
  }
  .canvas { position: relative; width: 1200px; height: 960px; }

  .card-front {
    position: absolute; left: 302px; top: 129px; width: 600px; height: 342px;
    background: linear-gradient(135deg, var(--paper-a), var(--paper-b));
    overflow: hidden;
  }
  .card-front .brand-name {
    position: absolute; right: 37px; top: 64px;
    font-family: "Michroma", sans-serif; font-size: 21px; color: var(--navy);
    letter-spacing: 0.5px; white-space: nowrap;
  }
  .holder-name {
    position: absolute; left: 33px; top: 212px;
    font-family: "Michroma", sans-serif; font-size: 15px; font-weight: 400; color: var(--navy);
    letter-spacing: 0; text-transform: uppercase; white-space: nowrap;
  }
  .name-rule {
    position: absolute; left: 33px; top: 245px; width: 530px; height: 2px;
    background: var(--green);
  }
  .contact-list {
    position: absolute; left: 33px; top: 258px; list-style: none;
    font-family: "Roboto", sans-serif; font-size: 14px; color: var(--ink); line-height: 18px;
  }
  .contact-list li { display: flex; align-items: center; gap: 6px; }
  .contact-list svg { width: 12px; height: 12px; fill: var(--navy); }
  .address {
    position: absolute; right: 35px; top: 258px; text-align: right; font-style: normal;
    font-family: "Roboto", sans-serif; font-size: 14px; color: var(--ink); line-height: 18px;
  }
  .footer-band { position: absolute; left: 0; bottom: 0; width: 600px; height: 32px; }
  .website {
    position: absolute; right: 27px; bottom: 9px;
    font-family: "Roboto", sans-serif; font-size: 13px; color: var(--green);
    letter-spacing: 1.6px;
  }

  .card-back {
    position: absolute; left: 299px; top: 488px; width: 600px; height: 343px;
    background: linear-gradient(150deg, var(--navy-light) 0%, var(--navy-deep) 45%, var(--navy-deep) 100%);
    display: flex; align-items: center; justify-content: center;
  }
  .card-back .brand-name {
    font-family: "Michroma", sans-serif; font-size: 28px; color: var(--white);
    letter-spacing: 1px; white-space: nowrap;
  }
</style>
</head>
<body>
<main class="canvas">
  <section class="card-front">
    <div class="brand-name">LUMEN FILEDESK</div>
    <h1 class="holder-name">Marcus L. Tembrook, CPA</h1>
    <div class="name-rule"></div>
    <ul class="contact-list">
      <li><svg viewBox="0 0 24 24" aria-hidden="true"><path d="M6.6 10.8a15.1 15.1 0 0 0 6.6 6.6l2.2-2.2a1 1 0 0 1 1-.25 11.4 11.4 0 0 0 3.6.57 1 1 0 0 1 1 1V20a1 1 0 0 1-1 1A17 17 0 0 1 3 4a1 1 0 0 1 1-1h3.5a1 1 0 0 1 1 1c0 1.25.2 2.45.57 3.6a1 1 0 0 1-.25 1z"/></svg>712-555-0172</li>
      <li><svg viewBox="0 0 24 24" aria-hidden="true"><path d="M2 5h20v14H2z M3 6l9 7 9-7" fill="var(--navy)" stroke="#fff" stroke-width="1.5"/></svg>marcus@lumenfiledesk.com</li>
    </ul>
    <address class="address">482 E Larkin Ave<br>Alder Falls, WI 53911</address>
    <svg class="footer-band" viewBox="0 0 600 32" aria-hidden="true">
      <rect x="0" y="24" width="600" height="8" fill="var(--navy)"/>
      <polygon points="350,32 374,1 588,1 588,32" fill="var(--navy)"/>
      <rect x="589" y="1" width="11" height="31" fill="var(--green)"/>
    </svg>
    <div class="website">www.lumenfiledesk.com</div>
  </section>

  <section class="card-back">
    <div class="brand-name">LUMEN FILEDESK</div>
  </section>
</main>
</body>
</html>
```